We are a General Practice - Family medicine
We also have Allied Health professionals working within our team

Industry/Entity Type

Business

Contact Information for Business Card

Front of the card to display:

HARBOURVIEW MEDICAL
PHONE 6381 2947

5/14 Kellerton Avenue
Launceston Tasmania 7268

Back of the card to display:

My Appointments
Date:
Time:
With:

Please remember to phone us on 6381 2947 to cancel your appointment if you can't keep it.
A fee applied to missed appointments

```html
<!DOCTYPE html>
<html lang="en">
<head>
<meta charset="utf-8">
<title>Harbourview Medical – Appointment Card</title>
<link href="https://fonts.googleapis.com/css2?family=Quicksand:wght@500;600&display=swap" rel="stylesheet">
<style>
  :root{
    --bg:#cadfd5;
    --card:#ffffff;
    --sky:#45c0e8;
    --leaf:#8fd43a;
    --ink:#6d7274;
    --panel:#e9ecea;
    --rule:#8a8f91;
  }
  *{box-sizing:border-box;margin:0;padding:0}
  html,body{width:1200px;height:1000px;overflow:hidden}
  body{
    background:var(--bg);
    font-family:"Quicksand",sans-serif;
    position:relative;
  }
  .card{
    position:absolute;
    left:250px;
    width:700px;height:400px;
    background:var(--card);
    border-radius:34px;
    box-shadow:0 6px 18px rgba(60,90,80,.18);
  }
  .card--front{top:70px}
  .card--back{top:530px}

  .brand{display:flex;align-items:center;gap:14px}
  .brand__dot{width:34px;height:34px;border-radius:50%;background:var(--leaf);flex:none}
  .brand__name{font-weight:600;color:var(--sky);font-size:40px;letter-spacing:.5px;line-height:1}
  .brand__tag{font-weight:600;color:var(--ink);font-size:11px;letter-spacing:4px;text-transform:uppercase}

  /* front */
  .front__inner{position:absolute;inset:0;display:flex;flex-direction:column;align-items:center;justify-content:center}
  .front__tag{margin-top:8px}
  .front__phone{margin-top:26px;color:var(--sky);font-weight:600;font-size:46px;letter-spacing:3px}
  .front__address{margin-top:18px;color:var(--leaf);font-weight:600;font-size:21px;letter-spacing:2px;text-align:center;line-height:1.35}

  /* back */
  .back__brand{position:absolute;left:70px;top:36px}
  .back__brand .brand__name{font-size:30px}
  .back__brand .brand__dot{width:26px;height:26px}
  .back__tag{position:absolute;left:110px;top:74px;font-size:9px;letter-spacing:3.5px}
  .panel{
    position:absolute;left:150px;top:104px;width:490px;height:170px;
    background:var(--panel);border-radius:10px;padding:14px 26px 0;
  }
  .panel__title{text-align:center;color:var(--ink);font-weight:600;font-size:18px;letter-spacing:6px;text-transform:uppercase;margin-bottom:14px}
  .field{display:flex;align-items:flex-end;gap:10px;height:38px;color:var(--ink);font-weight:600;font-size:17px;letter-spacing:2px}
  .field__line{flex:1;border-bottom:1.5px solid var(--rule);margin-bottom:6px}
  .notice{position:absolute;left:60px;right:60px;top:292px;text-align:center;font-weight:600;font-size:19px;line-height:1.35}
  .notice__remind{color:var(--leaf)}
  .notice__fee{color:var(--sky);margin-top:6px}
</style>
</head>
<body>
  <section class="card card--front" aria-label="Card front">
    <div class="front__inner">
      <div class="brand">
        <span class="brand__dot"></span>
        <span class="brand__name">Harbourview Medical</span>
      </div>
      <div class="brand__tag front__tag">Healthcare Centre</div>
      <div class="front__phone">6381 2947</div>
      <div class="front__address">5/14 Kellerton Avenue<br>Launceston Tasmania 7268</div>
    </div>
  </section>

  <section class="card card--back" aria-label="Card back">
    <div class="brand back__brand">
      <span class="brand__dot"></span>
      <span class="brand__name">Harbourview Medical</span>
    </div>
    <div class="brand__tag back__tag">Healthcare Centre</div>
    <div class="panel">
      <div class="panel__title">My Appointments</div>
      <div class="field"><span>DATE:</span><span class="field__line"></span></div>
      <div class="field"><span>TIME:</span><span class="field__line"></span></div>
      <div class="field"><span>WITH:</span><span class="field__line"></span></div>
    </div>
    <div class="notice">
      <p class="notice__remind">Please remember to phone us on 6381 2947<br>to cancel your appointment if you can't keep it.</p>
      <p class="notice__fee">A fee applied to missed appointments</p>
    </div>
  </section>
</body>
</html>
```